Lumo -Fresh business card design

It is a dry cleaning carpet business.
Red wine stain removal and pet urine treatments.
Servicing all regional areas.
Updates

all logo and pictures files have been uploaded

Industry/Entity Type

Dry Cleaning

Contact Information for Business Card

Lumo-Fresh Carpet and upholstery cleaning.
Servicing Albury/Wodonga and surrounding areas.
ph gus 0461273904 ,email lumofresh1@tealpost.example

Font styles to use
Serif
Sans Serif
Other font styles liked:
• lumo fresh logo font

Colors
ec2027
ffcf3e
33a6d7
0692cd

Requirements
Nice to have
• I have included photos of the logo and car and stripe on van ,I dont need all of them in the card just i would like to stick to these colours.

```html
<!DOCTYPE html>
<html lang="en">
<head>
<meta charset="utf-8">
<title>Lumo-Fresh Business Card</title>
<link rel="stylesheet" href="https://fonts.googleapis.com/css2?family=Open+Sans:wght@400;600;800&display=swap">
<style>
  :root {
    --backdrop: #3b3c3f;
    --card: #ffffff;
    --ink: #1e1e1e;
    --brand-blue: #0692cd;
    --sky-blue: #33a6d7;
    --band-end: #3e46a6;
    --tagline: #5a8fd6;
    --accent-yellow: #ffcf3e;
    --icon: #ffffff;
  }
  * { box-sizing: border-box; margin: 0; padding: 0; }
  html, body {
    width: 1200px;
    height: 816px;
    overflow: hidden;
    background: var(--backdrop);
  }
  .business-card {
    position: absolute;
    left: 80px;
    top: 108px;
    width: 1040px;
    height: 600px;
    background: var(--card);
    border-radius: 48px;
    overflow: hidden;
    font-family: "Open Sans", Arial, sans-serif;
    color: var(--ink);
  }
  .contact-band {
    position: absolute;
    left: 64px;
    top: 0;
    width: 46px;
    height: 520px;
    border-radius: 0 0 23px 23px;
    background: linear-gradient(180deg, var(--brand-blue) 0%, var(--sky-blue) 35%, #2f7fd0 65%, var(--band-end) 100%);
  }
  .band-icon {
    position: absolute;
    left: 9px;
    width: 28px;
    height: 28px;
    fill: var(--icon);
  }
  .icon-person { top: 104px; }
  .icon-phone  { top: 262px; }
  .icon-mail   { top: 316px; }
  .icon-web    { top: 358px; }
  .icon-home   { top: 440px; }

  .holder {
    position: absolute;
    left: 140px;
    top: 96px;
    line-height: 1.3;
  }
  .holder-name {
    font-size: 30px;
    font-weight: 400;
    letter-spacing: 0.5px;
  }
  .holder-role {
    font-size: 27px;
    font-weight: 400;
    letter-spacing: 1px;
  }
  .contact-line {
    position: absolute;
    left: 140px;
    font-size: 24px;
    line-height: 1.35;
  }
  .contact-phone { top: 258px; }
  .contact-mail  { top: 312px; }
  .contact-web   { top: 352px; }
  .contact-address { top: 418px; }

  .brand {
    position: absolute;
    left: 500px;
    top: 150px;
    width: 440px;
    text-align: center;
  }
  .brand-name {
    font-size: 76px;
    font-weight: 800;
    color: var(--brand-blue);
    letter-spacing: 1px;
    line-height: 1;
  }
  .brand-tagline {
    margin-top: 10px;
    font-size: 29px;
    font-weight: 600;
    color: var(--tagline);
    line-height: 1.15;
  }
  .accent-bar {
    position: absolute;
    right: 0;
    top: 196px;
    width: 70px;
    height: 26px;
    background: var(--accent-yellow);
  }
</style>
</head>
<body>
  <main class="business-card">
    <div class="contact-band">
      <svg class="band-icon icon-person" viewBox="0 0 24 24" aria-hidden="true">
        <circle cx="12" cy="8" r="5"/>
        <path d="M2 23c0-6 4.5-9 10-9s10 3 10 9z"/>
      </svg>
      <svg class="band-icon icon-phone" viewBox="0 0 24 24" aria-hidden="true">
        <path d="M6.6 2.5l3 3.2-1.8 2.6c1.2 2.8 3.1 4.7 5.9 5.9l2.6-1.8 3.2 3-1.6 3.6C11 19 5 13 3 4.1z"/>
      </svg>
      <svg class="band-icon icon-mail" viewBox="0 0 24 24" aria-hidden="true">
        <path d="M2 5h20v14H2z M3.5 6.5L12 13l8.5-6.5" stroke="#2f7fd0" stroke-width="1.5"/>
      </svg>
      <svg class="band-icon icon-web" viewBox="0 0 24 24" aria-hidden="true">
        <path fill="none" stroke="#ffffff" stroke-width="1.8" d="M12 2a10 10 0 1 0 0 20a10 10 0 1 0 0-20z M2 12h20 M12 2c-3.5 3-3.5 17 0 20 M12 2c3.5 3 3.5 17 0 20 M4 7h16 M4 17h16"/>
      </svg>
      <svg class="band-icon icon-home" viewBox="0 0 24 24" aria-hidden="true">
        <path d="M12 2L1 12h3v10h6v-6h4v6h6V12h3z"/>
      </svg>
    </div>

    <div class="holder">
      <p class="holder-name">nora whitfield</p>
      <p class="holder-role">GENERAL MANAGER</p>
    </div>

    <p class="contact-line contact-phone">+2 (0155) 48-710-36</p>
    <p class="contact-line contact-mail">hello@lumomail.example</p>
    <p class="contact-line contact-web">www.lumofresh.example</p>
    <p class="contact-line contact-address">418 Kiewa Street AVE,<br>North Albury, AUS</p>

    <div class="brand">
      <p class="brand-name">Lumo-Fresh</p>
      <p class="brand-tagline">CARPET &amp; UPHOLSTERY<br>CLEANING</p>
    </div>

    <div class="accent-bar"></div>
  </main>
</body>
</html>
```